Brookmere Osteopathy flyer

I want a clean clear DL flyer (but also want an A4 poster) promoting a new Osteopathic business in a semi rural area in Tasmania (Australia).
It can have pictures like the examples attached to show people what Osteopathy is (its like Chiropractic and physiotherapy).
I am the sole practioner and am male, so any pictures would be best to be a white male if possible.
I've attached some wording, you can use all, or none of it
I don't have a phone number for the business yet
info@brookmereosteopathy.example
www.brookmereosteopathy.example
Target Market(s)
Australians, from tradies, professionals, babies to retired people
Industry/Entity Type
Health
Look and feel

```html
<!DOCTYPE html>
<html lang="en">
<head>
<meta charset="utf-8">
<title>Brookmere Osteopathy – DL Flyer</title>
<link rel="stylesheet" href="https://fonts.googleapis.com/css2?family=Sorts+Mill+Goudy&family=Open+Sans:wght@400;700;800&family=Open+Sans+Condensed:wght@700&family=Signika:wght@600&family=Poppins:wght@400;700&display=swap">
<style>
  :root {
    --canvas: #e8e8e8;
    --navy: #1a2b5c;
    --navy-deep: #15244d;
    --royal: #2a4fa3;
    --sky: #1b98d5;
    --sky-light: #bfe0f5;
    --orange: #f7943a;
    --white: #ffffff;
    --grey-text: #4a4f5c;
  }
  * { box-sizing: border-box; margin: 0; padding: 0; }
  html, body { width: 1200px; height: 1134px; overflow: hidden; background: var(--canvas); }

  .flyer {
    position: absolute;
    top: 161px;
    width: 403px;
    height: 853px;
    overflow: hidden;
    background: var(--navy);
  }
  .flyer--services { left: 168px; }
  .flyer--intro { left: 644px; background: linear-gradient(160deg, var(--royal) 0%, var(--navy) 55%, var(--navy-deep) 100%); }

  .flyer__art { position: absolute; inset: 0; width: 403px; height: 853px; }

  /* Services side */
  .services-tab {
    position: absolute; left: 0; top: 42px;
    width: 300px; height: 38px;
    background: var(--orange);
    clip-path: polygon(0 0, 100% 0, 93% 100%, 0 100%);
    border-radius: 0 8px 8px 0;
  }
  .services-tab__title {
    position: absolute; left: 40px; top: 3px;
    font-family: "Sorts Mill Goudy", serif;
    font-size: 26px; color: var(--white); letter-spacing: 0.5px;
  }
  .services-list {
    position: absolute; left: 32px; top: 96px;
    list-style: none;
    font-family: "Sorts Mill Goudy", serif;
    font-size: 19.6px; color: var(--white);
  }
  .services-list li { height: 30.8px; display: flex; align-items: center; gap: 8px; white-space: nowrap; }
  .services-list svg { width: 14px; height: 14px; flex: none; }

  .brand-name {
    position: absolute; left: 34px; top: 430px;
    font-family: "Open Sans", sans-serif; font-weight: 800; line-height: 1;
  }
  .brand-name__main { display: block; font-size: 30px; color: var(--orange); }
  .brand-name__sub { display: block; font-size: 22px; color: var(--white); margin-top: 6px; }

  .name-badge {
    position: absolute;
    border-radius: 50%;
    background: var(--white);
    display: flex; align-items: center; justify-content: center; text-align: center;
    font-family: "Open Sans", sans-serif; font-weight: 700; color: var(--navy);
    box-shadow: 0 4px 10px rgba(0,0,0,0.25);
  }
  .name-badge--services { left: 189px; top: 611px; width: 166px; height: 166px; font-size: 17px; line-height: 1.25; }
  .name-badge--intro { left: 72px; top: 436px; width: 202px; height: 202px; font-size: 20px; line-height: 1.25; }

  .phone-line {
    position: absolute; right: 20px; top: 782px;
    display: flex; align-items: center; gap: 6px;
    font-family: "Open Sans Condensed", "Open Sans", sans-serif; font-weight: 700;
    font-size: 28px; line-height: 34px; color: var(--white);
  }
  .web-line {
    position: absolute; right: 20px; top: 821px;
    font-family: "Open Sans", sans-serif; font-weight: 700;
    font-size: 12px; line-height: 16px; color: var(--navy); letter-spacing: 0.2px;
    white-space: nowrap;
  }

  /* Intro side */
  .intro-question {
    position: absolute; right: 24px; top: 28px; text-align: right;
  }
  .intro-question__lead {
    font-family: "Open Sans", sans-serif; font-weight: 400;
    font-size: 18px; color: var(--grey-text);
  }
  .intro-question__headline {
    font-family: "Signika", sans-serif; font-weight: 600;
    font-size: 25px; line-height: 28px; color: var(--orange); margin-top: 2px;
  }
  .intro-copy {
    position: absolute; left: 27px; top: 653px;
    font-family: "Poppins", sans-serif; font-size: 13.3px; line-height: 17.3px;
    color: var(--white); white-space: nowrap;
  }
  .intro-copy strong { font-weight: 700; }
  .intro-copy .accent { color: var(--orange); font-weight: 700; }

  .contact-band {
    position: absolute; left: 0; right: 0; bottom: 0; height: 93px;
    background: linear-gradient(90deg, rgba(20,45,95,0.9), rgba(25,60,115,0.6));
    clip-path: polygon(0 0, 83% 0, 100% 40%, 100% 100%, 0 100%);
  }
  .contact-list {
    position: absolute; left: 27px; top: 773px; list-style: none;
    font-family: "Open Sans", sans-serif; font-size: 13px; color: var(--white);
  }
  .contact-list li { height: 21.7px; display: flex; align-items: center; gap: 7px; white-space: nowrap; }
  .contact-list svg { width: 16px; height: 16px; flex: none; }
</style>
</head>
<body>

<section class="flyer flyer--services">
  <svg class="flyer__art" viewBox="0 0 403 853">
    <defs>
      <linearGradient id="tennisTone" x1="0" y1="0" x2="0" y2="1">
        <stop offset="0" stop-color="#8fb9de"/>
        <stop offset="0.45" stop-color="#6e9a4c"/>
        <stop offset="1" stop-color="#c9703f"/>
      </linearGradient>
      <linearGradient id="neckTone" x1="0" y1="0" x2="1" y2="1">
        <stop offset="0" stop-color="#d9d6d2"/>
        <stop offset="0.5" stop-color="#c7b6a4"/>
        <stop offset="1" stop-color="#8e8f92"/>
      </linearGradient>
    </defs>
    <path d="M403 676 C330 700 260 770 200 810 C140 845 60 852 0 846 V853 H403 Z" fill="var(--sky)"/>
    <path d="M403 640 V853 H150 C220 830 280 770 330 720 C360 690 385 672 403 660 Z" fill="var(--sky)"/>
    <g role="img" aria-label="Photo: young tennis player holding her sore shoulder on a clay court">
      <circle cx="335" cy="547" r="148" fill="url(#tennisTone)"/>
    </g>
    <g role="img" aria-label="Photo: older woman wincing and rubbing her painful neck">
      <circle cx="63" cy="671" r="162" fill="url(#neckTone)"/>
    </g>
  </svg>

  <div class="services-tab"><span class="services-tab__title">Services included:</span></div>

  <ul class="services-list">
    <li><svg viewBox="0 0 14 14"><polyline points="1.5,7.5 5.5,11.5 12.5,2.5" fill="none" stroke="var(--orange)" stroke-width="2.4" stroke-linecap="round" stroke-linejoin="round"/></svg>Back / neck pain</li>
    <li><svg viewBox="0 0 14 14"><polyline points="1.5,7.5 5.5,11.5 12.5,2.5" fill="none" stroke="var(--orange)" stroke-width="2.4" stroke-linecap="round" stroke-linejoin="round"/></svg>Headaches / migraines</li>
    <li><svg viewBox="0 0 14 14"><polyline points="1.5,7.5 5.5,11.5 12.5,2.5" fill="none" stroke="var(--orange)" stroke-width="2.4" stroke-linecap="round" stroke-linejoin="round"/></svg>Joint and muscle pain</li>
    <li><svg viewBox="0 0 14 14"><polyline points="1.5,7.5 5.5,11.5 12.5,2.5" fill="none" stroke="var(--orange)" stroke-width="2.4" stroke-linecap="round" stroke-linejoin="round"/></svg>Pregnancy-related discomfort</li>
    <li><svg viewBox="0 0 14 14"><polyline points="1.5,7.5 5.5,11.5 12.5,2.5" fill="none" stroke="var(--orange)" stroke-width="2.4" stroke-linecap="round" stroke-linejoin="round"/></svg>Disc related issues</li>
    <li><svg viewBox="0 0 14 14"><polyline points="1.5,7.5 5.5,11.5 12.5,2.5" fill="none" stroke="var(--orange)" stroke-width="2.4" stroke-linecap="round" stroke-linejoin="round"/></svg>Sciatica</li>
    <li><svg viewBox="0 0 14 14"><polyline points="1.5,7.5 5.5,11.5 12.5,2.5" fill="none" stroke="var(--orange)" stroke-width="2.4" stroke-linecap="round" stroke-linejoin="round"/></svg>Plantar fasciitis</li>
    <li><svg viewBox="0 0 14 14"><polyline points="1.5,7.5 5.5,11.5 12.5,2.5" fill="none" stroke="var(--orange)" stroke-width="2.4" stroke-linecap="round" stroke-linejoin="round"/></svg>Tendonitis / Bursitis</li>
    <li><svg viewBox="0 0 14 14"><polyline points="1.5,7.5 5.5,11.5 12.5,2.5" fill="none" stroke="var(--orange)" stroke-width="2.4" stroke-linecap="round" stroke-linejoin="round"/></svg>Adhesive capsulitis (frozen shoulder)</li>
    <li><svg viewBox="0 0 14 14"><polyline points="1.5,7.5 5.5,11.5 12.5,2.5" fill="none" stroke="var(--orange)" stroke-width="2.4" stroke-linecap="round" stroke-linejoin="round"/></svg>Tennis / Golfers elbow</li>
  </ul>

  <h1 class="brand-name">
    <span class="brand-name__main">Brookmere</span>
    <span class="brand-name__sub">Osteopathy</span>
  </h1>

  <div class="name-badge name-badge--services">Brookmere<br>Osteopathy</div>

  <div class="phone-line">
    <svg width="27" height="27" viewBox="0 0 24 24" aria-hidden="true"><circle cx="12" cy="12" r="12" fill="var(--orange)"/><path d="M8.3 5.8l1.9 2.6-1.1 1.6c.7 1.6 2 2.9 3.6 3.6l1.6-1.1 2.6 1.9-1 2.4c-4.6-.2-8.4-4-8.6-8.6z" fill="var(--white)"/></svg>
    03 5550 1234
  </div>
  <div class="web-line">www.brookmereosteopathy.example</div>
</section>

<section class="flyer flyer--intro">
  <svg class="flyer__art" viewBox="0 0 403 853">
    <defs>
      <linearGradient id="clinicTone" x1="0" y1="0" x2="1" y2="1">
        <stop offset="0" stop-color="#f3f5f8"/>
        <stop offset="0.55" stop-color="#e4e9ef"/>
        <stop offset="1" stop-color="#c9d3de"/>
      </linearGradient>
    </defs>
    <path d="M150 0 H403 V330 C385 470 290 600 150 600 C70 600 20 585 0 570 V220 C25 120 80 45 150 0 Z" fill="var(--sky)" transform="translate(-12 4)"/>
    <path d="M150 0 H403 V330 C385 470 290 600 150 600 C70 600 20 585 0 570 V220 C25 120 80 45 150 0 Z" fill="var(--sky-light)" transform="translate(-5 2)"/>
    <g role="img" aria-label="Photo: osteopath treating a patient's back on a clinic table, with a faint spine graphic">
      <path d="M160 0 H403 V320 C385 460 290 585 155 585 C80 585 25 570 0 555 V215 C30 115 90 40 160 0 Z" fill="url(#clinicTone)"/>
    </g>
  </svg>

  <div class="intro-question">
    <p class="intro-question__lead">Are you suffering in</p>
    <h2 class="intro-question__headline">Back/Neck Pain or Other<br>Any Body Problems?</h2>
  </div>

  <div class="name-badge name-badge--intro">Brookmere<br>Osteopathy</div>

  <p class="intro-copy">
    <strong>Osteopaths use</strong> a combination of joint<br>
    manipulation, targeted <span class="accent">Deep tissue massage</span><br>
    and stretching to <span class="accent">Improve Function,</span><br>
    <span class="accent">Relieve Pain</span> and support the body’s<br>
    ability to <strong>heal itself</strong>.
  </p>

  <div class="contact-band"></div>
  <ul class="contact-list">
    <li><svg viewBox="0 0 24 24" aria-hidden="true"><circle cx="12" cy="12" r="12" fill="var(--orange)"/><path d="M8.3 5.8l1.9 2.6-1.1 1.6c.7 1.6 2 2.9 3.6 3.6l1.6-1.1 2.6 1.9-1 2.4c-4.6-.2-8.4-4-8.6-8.6z" fill="var(--white)"/></svg>03 5550 1234</li>
    <li><svg viewBox="0 0 24 24" aria-hidden="true"><circle cx="12" cy="12" r="12" fill="var(--orange)"/><rect x="6" y="8" width="12" height="8.5" rx="1" fill="var(--white)"/><polyline points="6.5,8.5 12,13 17.5,8.5" fill="none" stroke="var(--orange)" stroke-width="1.3"/></svg>info@brookmereosteopathy.example</li>
    <li><svg viewBox="0 0 24 24" aria-hidden="true"><circle cx="12" cy="12" r="12" fill="var(--orange)"/><path d="M12 5a4.5 4.5 0 0 0-4.5 4.5c0 3.4 4.5 9 4.5 9s4.5-5.6 4.5-9A4.5 4.5 0 0 0 12 5z" fill="var(--white)"/><circle cx="12" cy="9.6" r="1.7" fill="var(--orange)"/></svg>24 Example Lane, Brookmere</li>
  </ul>
</section>

</body>
</html>
```